Single Page website for Product Company

I need a website designed for my small startup company "Yard Leisure Crafts". We design and manufacture custom innovative indoor/outdoor entertainment furnishings e.g. outdoor TV enclosures, outdoor bars and outdoor kitchens. I'm looking for a single page site based on the the shopLite-SoloPage-ecommerce bootstrap page, attached.

I've also attached pictures of my products, these need to be photoshopped and placed in an outdoor patio area if possible.

Target Market(s)

Home owners

Industry/Entity Type

It Company

Coding

Coded - Design and coding required

Number of Pages Required

1 page

Requirements
Must have
• Must be single page site built with attached bootstrap template and adjust to screen size e.g. ipad, mobile phone and computer
Nice to have
• Integration with vendora

```html
<!DOCTYPE html>
<html lang="en">
<head>
<meta charset="utf-8">
<title>Yard Leisure Crafts</title>
<link href="https://fonts.googleapis.com/css2?family=Roboto+Condensed:wght@300;400;700&family=Roboto:ital,wght@0,300;0,400;0,500;0,700;1,400&display=swap" rel="stylesheet">
<style>
:root{
  --orange:#f7941d;
  --blue:#3d8fdc;
  --ink:#333;
  --muted:#777;
  --light:#efefef;
  --line:#dcdcdc;
  --dark:#232323;
  --darker:#111;
  --white:#fff;
}
*{box-sizing:border-box;margin:0;padding:0}
html,body{width:1200px;height:3939px;overflow:hidden}
body{font-family:"Roboto",sans-serif;color:var(--ink);background:var(--white);position:relative}
section,header,footer{position:absolute;left:0;width:1200px;overflow:hidden}
.abs{position:absolute}
.photo{position:absolute}

/* hero */
.hero{top:0;height:622px}
.hero .photo{inset:0;background:linear-gradient(180deg,#3f4a3a 0%,#5b604c 35%,#4a3f33 65%,#2d2620 100%)}
.hero .shade{position:absolute;inset:0;background:rgba(0,0,0,.25)}
.brand{left:110px;top:30px;font:500 26px "Roboto",sans-serif;color:var(--blue);display:flex;align-items:center;gap:10px}
.brand i{width:22px;height:22px;background:var(--orange);display:block;border-radius:50%}
.nav{right:100px;top:40px;display:flex;gap:30px;align-items:center;font:500 14px "Roboto",sans-serif;color:var(--white);letter-spacing:.3px}
.cart{width:30px;height:30px;border:1.5px solid var(--white);border-radius:50%;display:flex;align-items:center;justify-content:center;position:relative}
.cart b{position:absolute;top:-4px;right:-4px;width:9px;height:9px;background:var(--orange);border-radius:50%}
.hero h1{top:292px;width:100%;text-align:center;font:700 46px "Roboto Condensed",sans-serif;color:var(--white)}
.hero p{top:348px;width:100%;text-align:center;font:400 13px/19px "Roboto",sans-serif;color:#eee}
.btn-ghost{left:528px;top:405px;width:144px;height:42px;border:1.5px solid var(--white);color:var(--white);font:400 14px "Roboto",sans-serif;display:flex;align-items:center;justify-content:center}
.dots{top:558px;left:0;width:100%;display:flex;justify-content:center;gap:8px}
.dots span{width:12px;height:12px;border-radius:50%;border:1.5px solid var(--white)}
.dots span.on{background:var(--white)}

/* products */
.products{top:622px;height:573px}
.section-title{width:100%;text-align:center;font:300 32px "Roboto Condensed",sans-serif;color:var(--ink)}
.products .section-title{top:52px}
.card{top:132px;width:487px}
.card .photo{position:relative;height:318px;border-radius:6px;background:linear-gradient(160deg,#7c8a92 0%,#a08670 45%,#5a4a3e 100%)}
.card .cap{display:flex;justify-content:space-between;margin-top:16px;font:400 17px "Roboto",sans-serif;color:#555}
.card .cap b{color:var(--orange);font-weight:400}

/* shipping */
.shipping{top:1195px;height:249px;background:var(--light)}
.shipping h2{top:48px;width:100%;text-align:center;font:400 33px "Roboto Condensed",sans-serif;color:var(--ink)}
.shipping .timer{top:88px;width:100%;text-align:center;font:400 38px "Roboto Condensed",sans-serif;color:var(--ink)}
.btn-blue{left:523px;top:163px;width:150px;height:40px;background:var(--blue);color:var(--white);font:500 14px "Roboto",sans-serif;display:flex;align-items:center;justify-content:center;border-radius:3px}

/* welcome */
.welcome{top:1444px;height:478px;background:#1d1915}
.welcome .right{position:absolute;left:600px;top:0;width:600px;height:478px;background:linear-gradient(135deg,#3a2e24,#1c1814 60%,#2a231c)}
.welcome .left{position:absolute;left:0;top:0;width:600px;height:478px;clip-path:polygon(0 36px,600px 0,600px 478px,0 478px);background:linear-gradient(160deg,#d9c9a8 0%,#b8a486 45%,#8d7a62 100%)}
.welcome .copy{left:643px;top:122px;width:480px;color:var(--white)}
.welcome h2{font:400 34px "Roboto Condensed",sans-serif}
.welcome h3{font:400 21px "Roboto Condensed",sans-serif;margin-top:4px}
.welcome p{font:400 11.5px/17px "Roboto",sans-serif;color:#ddd;margin-top:14px}
.ticks{list-style:none;margin-top:14px}
.ticks li{font:400 12.5px "Roboto",sans-serif;color:#eee;display:flex;gap:12px;align-items:center;height:30px}

/* testimonial */
.testimonial{top:1922px;height:239px}
.testimonial blockquote{top:52px;left:236px;width:728px;text-align:center;font:italic 400 13px/25px "Roboto",sans-serif;color:var(--muted)}
.testimonial cite{top:138px;width:100%;text-align:center;font:italic 400 15px "Roboto",sans-serif;color:var(--blue)}
.testimonial .bar{top:192px;left:560px;width:80px;height:3px;background:#e4e4e4}
.testimonial .bar i{display:block;width:28px;height:3px;background:var(--blue)}

/* newsletter */
.newsletter{top:2161px;height:155px;border-top:1px solid #eee}
.nl-icon{left:178px;top:50px;width:54px;height:54px;border-radius:50%;background:var(--orange);display:flex;align-items:center;justify-content:center}
.nl-text{left:250px;top:49px}
.nl-text h4{font:400 24px "Roboto Condensed",sans-serif;color:var(--ink)}
.nl-text p{font:400 14px "Roboto",sans-serif;color:var(--muted);margin-top:4px}
.nl-input{left:548px;top:58px;width:312px;height:42px;border:1px solid var(--line);font:400 12px "Roboto",sans-serif;color:#999;padding:14px 12px}
.nl-btn{left:860px;top:58px;width:128px;height:42px;background:var(--orange);color:var(--white);font:500 13px "Roboto",sans-serif;display:flex;align-items:center;justify-content:center}

/* order form */
.order{top:2316px;height:848px;background:var(--light)}
.order .section-title{top:65px}
.table{left:98px;top:146px;width:1003px;background:var(--white);font:400 13px "Roboto",sans-serif;color:#666}
.table .row{display:grid;grid-template-columns:356px 255px 265px 127px;height:42px;align-items:center;border-top:1px solid #eee}
.table .row:first-child{border-top:0;height:48px;color:#444}
.table .row span:nth-child(1){padding-left:94px}
.qty{display:inline-flex;width:56px;height:22px;border:1px solid var(--line);align-items:center;justify-content:space-between;padding:0 6px;font-size:11px;font-style:normal}
.col{top:355px;width:476px}
.col h5{font:400 17px "Roboto",sans-serif;color:var(--ink);margin:0 0 10px}
.field{height:42px;background:var(--white);border:1px solid var(--line);font:400 12px "Roboto",sans-serif;color:#888;display:flex;align-items:center;justify-content:space-between;padding:0 12px;margin-bottom:10px}
.pair{display:flex;gap:14px}
.pair .field{flex:1}
.caret{font-size:9px;color:#555}
.coupon{display:flex}
.coupon .field{flex:1;margin:0}
.coupon .go{width:94px;height:42px;background:var(--orange);color:var(--white);font:500 12px "Roboto",sans-serif;display:flex;align-items:center;justify-content:center}
.summary{background:var(--white);border:1px solid var(--line);font:400 12px "Roboto",sans-serif;color:#666}
.summary div{display:flex;justify-content:space-between;padding:0 14px;height:42px;align-items:center}
.summary div+div{border-top:1px solid #eee}
.btn-orange{width:186px;height:42px;background:var(--orange);color:var(--white);font:500 15px "Roboto",sans-serif;display:flex;align-items:center;justify-content:center;margin-top:12px}

/* features */
.features{top:3164px;height:271px;background:linear-gradient(180deg,#3e8ed6,#2f7cc4)}
.feature{top:80px;width:260px;text-align:center;color:var(--white);font:400 24px "Roboto",sans-serif}
.feature svg{display:block;margin:0 auto 18px}

/* contact */
.contact{top:3435px;height:446px;background:var(--dark)}
.contact h3{font:400 32px "Roboto Condensed",sans-serif;color:var(--white)}
.citem{display:flex;gap:22px;align-items:flex-start;margin-bottom:22px;color:#ddd;font:400 12.5px/19px "Roboto",sans-serif}
.cicon{width:38px;height:38px;border-radius:50%;background:#3a3a3a;border:1px solid #555;display:flex;align-items:center;justify-content:center;flex:none}
.social{display:flex;gap:16px;margin-top:12px}
.social i{width:22px;height:22px;background:#ddd;border-radius:3px;display:block}
.msg-field{width:525px;height:36px;background:var(--white);margin-bottom:14px;font:400 12px "Roboto",sans-serif;color:#888;padding:11px 12px}
.msg-area{height:108px}
.submit{width:94px;height:36px;background:#f26b1d;color:var(--white);font:500 14px "Roboto",sans-serif;display:flex;align-items:center;justify-content:center}

/* bottom bar */
.bottom{top:3881px;height:58px;background:var(--darker)}
.bottom p{left:100px;top:22px;font:400 11px "Roboto",sans-serif;color:#ccc}
.cards{right:70px;top:14px;display:flex;gap:6px}
.cards i{display:block;width:44px;height:28px;background:#e8e8e8;border-radius:3px}
</style>
</head>
<body>

<header class="hero">
  <div class="photo" role="img" aria-label="Photo of a covered outdoor patio with wicker chairs in front of a stone TV enclosure with built-in speakers, forest behind"></div>
  <div class="shade"></div>
  <div class="abs brand"><i></i>Yard Leisure Crafts</div>
  <nav class="abs nav">
    <span>PRODUCTS</span><span>ABOUT</span><span>ORDER</span><span>CONTACT</span><span>EXTERNAL LINK</span>
    <svg width="16" height="16" viewBox="0 0 16 16"><circle cx="6.5" cy="6.5" r="5" fill="none" stroke="#fff" stroke-width="2"/><line x1="10.5" y1="10.5" x2="15" y2="15" stroke="#fff" stroke-width="2"/></svg>
    <span class="cart"><svg width="14" height="13" viewBox="0 0 14 13"><path d="M0 1h2.5l2 7h7l2-5H4" fill="none" stroke="#fff" stroke-width="1.5"/><circle cx="5.5" cy="11" r="1.2" fill="#fff"/><circle cx="10.5" cy="11" r="1.2" fill="#fff"/></svg><b></b></span>
  </nav>
  <h1 class="abs">YARD LEISURE CRAFTS</h1>
  <p class="abs">Custom outdoor enclosures, bars and kitchens built to last through every season and<br>every gathering, designed around the way your family enjoys the yard.</p>
  <div class="abs btn-ghost">FIND OUT MORE</div>
  <div class="abs dots"><span class="on"></span><span></span><span></span></div>
</header>

<section class="products">
  <h2 class="abs section-title">OUR PRODUCTS</h2>
  <div class="abs card" style="left:98px">
    <div class="photo" role="img" aria-label="Product photo: stone-clad TV enclosure with speakers on a patio beside a fire bowl"></div>
    <div class="cap"><span>Sed ut perspiciatis unde</span><b>$700</b></div>
  </div>
  <div class="abs card" style="left:614px">
    <div class="photo" role="img" aria-label="Product photo: grey stone TV enclosure with speakers on a patio with outdoor seating"></div>
    <div class="cap"><span>Sed ut perspiciatis unde</span><b>$700</b></div>
  </div>
</section>

<section class="shipping">
  <h2 class="abs">FREE INTERNATIONAL SHIPPING ONLY</h2>
  <div class="abs timer">2 days 23:37:36</div>
  <div class="abs btn-blue">ORDER NOW!</div>
</section>

<section class="welcome">
  <div class="right" role="img" aria-label="Dark photo of a covered outdoor entertainment area at dusk"></div>
  <div class="left" role="img" aria-label="Photo of a bright living room with a stone media unit, built-in speakers and a sofa"></div>
  <div class="abs copy">
    <h2>WELCOME TO</h2>
    <h3>YARD LEISURE CRAFTS</h3>
    <p>We design and build custom entertainment furnishings for indoor and outdoor living, from weatherproof TV enclosures to full outdoor kitchens, crafted to fit your space and made to be enjoyed year round.</p>
    <ul class="ticks">
      <li><svg width="14" height="12" viewBox="0 0 14 12"><path d="M1 6l4 4 8-9" fill="none" stroke="#fff" stroke-width="2.2"/></svg>Nemo enim ipsam voluptatem quia voluptas sit aspernatur</li>
      <li><svg width="14" height="12" viewBox="0 0 14 12"><path d="M1 6l4 4 8-9" fill="none" stroke="#fff" stroke-width="2.2"/></svg>Nemo enim ipsam voluptatem quia voluptas</li>
      <li><svg width="14" height="12" viewBox="0 0 14 12"><path d="M1 6l4 4 8-9" fill="none" stroke="#fff" stroke-width="2.2"/></svg>Duis aute irure dolor in reprehenderit in voluptate</li>
      <li><svg width="14" height="12" viewBox="0 0 14 12"><path d="M1 6l4 4 8-9" fill="none" stroke="#fff" stroke-width="2.2"/></svg>Nemo enim ipsam voluptatem quia voluptas</li>
    </ul>
  </div>
</section>

<section class="testimonial">
  <blockquote class="abs">“ Our new outdoor TV enclosure turned the back patio into the favourite room of the house. The team listened, sketched ideas with us and delivered a piece that looks great and holds up in every kind of weather, right down to the finish on the stone. Friends now ask where we found it every single time they come over for a game night .</blockquote>
  <cite class="abs">Dana Fielder - Yard Leisure Crafts</cite>
  <div class="abs bar"><i></i></div>
</section>

<section class="newsletter">
  <div class="abs nl-icon"><svg width="24" height="20" viewBox="0 0 24 20"><path d="M2 10 22 2 18 18 11 13z" fill="#fff"/><path d="M11 13 9 18 10 12z" fill="#fde3c2"/></svg></div>
  <div class="abs nl-text"><h4>Join our Newsletter.</h4><p>Stay up to date with the latest news.</p></div>
  <div class="abs nl-input">Name</div>
  <div class="abs nl-btn">SUBSCRIBE</div>
</section>

<section class="order">
  <h2 class="abs section-title">ORDER FORM</h2>
  <div class="abs table">
    <div class="row"><span>Product</span><span>Unit Cost</span><span>Quantity</span><span>Total</span></div>
    <div class="row"><span>Bed</span><span>$700</span><span><i class="qty">1<b class="caret">▼</b></i></span><span>$700</span></div>
    <div class="row"><span>Nightstand</span><span>$400</span><span><i class="qty">3<b class="caret">▼</b></i></span><span>$1,200</span></div>
    <div class="row"><span>Hammock</span><span>$600</span><span><i class="qty">0<b class="caret">▼</b></i></span><span>$0</span></div>
  </div>

  <div class="abs col" style="left:98px">
    <h5>Payment Method</h5>
    <div class="pair"><div class="field" style="flex:2.4">Card number</div><div class="field">Code</div></div>
    <div class="pair"><div class="field">January<span class="caret">▼</span></div><div class="field">2017<span class="caret">▼</span></div></div>
    <h5 style="margin-top:14px">Information</h5>
    <div class="pair"><div class="field">First name<span class="caret">▼</span></div><div class="field">Last name<span class="caret">▼</span></div></div>
    <div class="field">Your email</div>
    <h5 style="margin-top:16px">If you have Coupon code</h5>
    <div class="coupon"><div class="field">Coupon code</div><div class="go">CHECK!</div></div>
  </div>

  <div class="abs col" style="left:624px">
    <h5>Delivery address</h5>
    <div class="field">Street address</div>
    <div class="pair"><div class="field">Country<span class="caret">▼</span></div><div class="field">City</div></div>
    <div class="field">Post code<span class="caret">▼</span></div>
    <h5 style="margin-top:14px">Order summary</h5>
    <div class="summary"><div><span>Shipping cost:</span><span>Free</span></div><div><span>Total:</span><span>$1,900.00</span></div></div>
    <div class="btn-orange">ORDER PRODUCTS</div>
  </div>
</section>

<section class="features">
  <div class="abs feature" style="left:180px">
    <svg width="44" height="54" viewBox="0 0 44 54"><path d="M22 2 40 8v18c0 13-8 21-18 26C12 47 4 39 4 26V8z" fill="#fff"/><path d="M22 9v36c-7-4-12-10-12-19V13z" fill="#3a87cf"/></svg>Quality Guaranteed
  </div>
  <div class="abs feature" style="left:470px">
    <svg width="60" height="50" viewBox="0 0 60 50"><rect x="2" y="6" width="34" height="28" fill="#fff"/><path d="M38 14h12l8 10v10H38z" fill="#fff"/><circle cx="14" cy="40" r="6" fill="#fff" stroke="#3a87cf" stroke-width="3"/><circle cx="48" cy="40" r="6" fill="#fff" stroke="#3a87cf" stroke-width="3"/></svg>Home delivery
  </div>
  <div class="abs feature" style="left:775px">
    <svg width="44" height="54" viewBox="0 0 44 54"><path d="M10 24V14a12 12 0 0 1 24 0v2" fill="none" stroke="#fff" stroke-width="5"/><rect x="4" y="24" width="36" height="28" rx="2" fill="#fff"/></svg>Secure payment
  </div>
</section>

<section class="contact">
  <div class="abs" style="left:150px;top:70px;width:340px">
    <h3>CONTACT US</h3>
    <div style="margin-top:22px">
      <div class="citem"><span class="cicon"><svg width="12" height="16" viewBox="0 0 12 16"><path d="M6 0a6 6 0 0 1 6 6c0 4-6 10-6 10S0 10 0 6a6 6 0 0 1 6-6z" fill="#fff"/><circle cx="6" cy="6" r="2.2" fill="#3a3a3a"/></svg></span><span>Yard Leisure Crafts<br>418 Orchard Lane<br>Suite 12 Millbrook, Ohio 44901</span></div>
      <div class="citem"><span class="cicon"><svg width="16" height="12" viewBox="0 0 16 12"><rect x="0.5" y="0.5" width="15" height="11" fill="none" stroke="#fff"/><path d="M.5.5 8 7 15.5.5" fill="none" stroke="#fff"/></svg></span><span>E-mail:<br>hello@yardleisurecrafts.example</span></div>
      <div class="citem"><span class="cicon"><svg width="14" height="14" viewBox="0 0 14 14"><path d="M3 0l3 3-2 2c1 2 3 4 5 5l2-2 3 3-2 3C6 14 0 8 0 3z" fill="#fff"/></svg></span><span>Phone Number :<br>(1.555.014.2290)</span></div>
    </div>
    <div style="font:500 15px 'Roboto',sans-serif;color:#fff;margin-top:-6px">SOCIAL</div>
    <div class="social"><i></i><i></i><i></i><i></i><i></i></div>
  </div>
  <div class="abs" style="left:527px;top:70px">
    <h3>LEAVE A MESSAGE</h3>
    <div style="margin-top:22px">
      <div class="msg-field">Your name...</div>
      <div class="msg-field">Contact email...</div>
      <div class="msg-field msg-area">Message is required</div>
      <div class="submit">SUBMIT</div>
    </div>
  </div>
</section>

<footer class="bottom">
  <p class="abs">Yard Leisure Crafts © 2017. All Rights Reserved</p>
  <div class="abs cards"><i></i><i></i><i></i><i></i></div>
</footer>

</body>
</html>
```